Fastest Work at home Solution for Small Businesses

We need a web page for a product called *BrightHarbor*
We develop an innovative VPN Appliance (Model-Name ->Vela Two) that gives small business the possibility literally setup the possibility for Companies to let their employees work from home.
With our secure appliance we create safe connection between any business and the employee *working at home*
Our Products *Vela Two* are rolled out in minutes.
A. Employees can connect directly
B. Work from any location
C. All this without having to change the company firewall
Use case
=======
1. Go to our page
2. Select Product
3. Order
4. Connect to any Switch in the company
5. install software on employees laptop
***** INSTANT Connection ******
Target Market(s)
Businesses
Coding
Coded - Design and coding required
Number of Pages Required
3 page
Font styles to use
Look and feel
Each slider illustrates characteristics of the customer's brand and the style your logo design should communicate.

```html
<!DOCTYPE html>
<html lang="en">
<head>
<meta charset="utf-8">
<title>BrightHarbor – Work from home, instantly</title>
<link href="https://fonts.googleapis.com/css2?family=Poppins:wght@400;500;600;700;800&display=swap" rel="stylesheet">
<style>
:root{
  --navy:#1b2142;
  --blue:#1e3fb8;
  --blue-bright:#2f6bf0;
  --cyan:#34b8f0;
  --lavender:#eef0fb;
  --lavender-deep:#e2e5f7;
  --text:#5d6277;
  --muted:#9aa0b4;
  --card:#ffffff;
  --star:#f5a623;
  --line:#d9dcec;
}
*{box-sizing:border-box;margin:0;padding:0}
html,body{width:1200px;height:3392px;overflow:hidden}
body{font-family:"Poppins",Arial,sans-serif;color:var(--navy);background:#fff;position:relative}
.bg-waves{position:absolute;left:0;top:0;width:1200px;height:3392px;z-index:0}
section,header,footer{position:absolute;left:0;width:1200px;z-index:1}

/* header */
.site-header{top:0;height:64px;display:flex;align-items:center;padding:0 96px}
.brand{display:flex;align-items:center;gap:10px;font-weight:700;font-size:24px;color:var(--blue)}
.brand-mark{width:22px;height:22px;border-radius:50%;background:var(--blue)}
.main-nav{margin-left:auto;display:flex;align-items:center;gap:34px;font-size:12px;font-weight:600;color:var(--navy)}
.btn-login{border:2px solid var(--blue);color:var(--blue);padding:7px 22px;border-radius:4px}

/* hero */
.hero{top:200px;height:320px}
.hero-title{position:absolute;left:96px;top:36px;width:620px;font-size:40px;line-height:1.15;font-weight:800;letter-spacing:.5px;white-space:nowrap}
.hero-text{position:absolute;left:96px;top:154px;width:500px;font-size:12px;line-height:1.6;color:var(--text)}
.btn-primary{position:absolute;left:96px;top:232px;background:var(--blue);color:#fff;font-size:12px;font-weight:600;padding:15px 32px;border-radius:4px}
.hero-art{position:absolute;left:640px;top:-120px;width:440px;height:440px;border-radius:50%;background:radial-gradient(circle at 45% 45%,#4a8cf5,#2640c9 55%,rgba(52,184,240,.25) 75%,transparent 76%)}

/* section heads */
.eyebrow{font-size:10px;letter-spacing:2px;color:var(--muted);font-weight:500;text-transform:uppercase}
.section-title{font-size:26px;font-weight:700;color:var(--navy);margin-top:6px}
.section-title.centered::after,.section-title.left::after{content:"";display:block;width:44px;height:3px;background:var(--blue);margin:10px auto 0}
.section-title.left::after{margin-left:0}
.center{text-align:center}

/* features */
.features{top:712px}
.feature-title{font-size:22px;font-weight:600}
.feature-title strong{font-weight:800}
.feature-row{display:flex;justify-content:center;gap:44px;margin-top:88px}
.feature-card{width:262px;height:336px;background:var(--card);border-radius:6px;box-shadow:0 6px 24px rgba(30,40,100,.1);padding:18px}
.feature-art{height:210px;border-radius:4px;background:linear-gradient(160deg,#e9efff,#cbd9fb)}
.feature-card h3{font-size:11px;font-weight:700;margin-top:18px;text-align:center;text-transform:uppercase}
.feature-card p{font-size:10px;color:var(--text);text-align:center;line-height:1.5;margin-top:6px}

/* steps */
.how{top:1216px;height:800px}
.how-head{position:absolute;left:144px;top:0}
.step{position:absolute;width:210px;height:240px;background:var(--card);border-radius:6px;box-shadow:0 6px 24px rgba(30,40,100,.1);text-align:center;padding:30px 22px}
.step-num{position:absolute;top:-14px;left:91px;width:28px;height:28px;border-radius:50%;background:var(--blue);color:#fff;font-size:12px;font-weight:600;line-height:28px}
.step-icon{width:54px;height:54px;margin:16px auto 0}
.step h4{font-size:11px;font-weight:700;margin-top:16px;text-transform:uppercase}
.step p{font-size:10px;line-height:1.5;color:var(--text);margin-top:8px}
.connector{position:absolute;height:2px;background:var(--line)}

/* testimonials */
.testimonials{top:2128px}
.quotes{position:absolute;top:120px;left:0;width:1200px;height:270px}
.quote-card{position:absolute;top:0;width:300px;height:264px;background:#f4f5fb;border-radius:6px;padding:64px 22px 0}
.avatar{position:absolute;top:-22px;left:120px;width:62px;height:62px;border-radius:50%;background:linear-gradient(160deg,#e8c6a8,#8a6552);border:3px solid #fff}
.quote-lead{font-size:13px;font-style:italic;color:var(--navy);font-weight:500}
.quote-body{font-size:10px;line-height:1.55;color:var(--text);margin-top:8px}
.quote-meta{position:absolute;left:22px;right:22px;bottom:22px;display:flex;justify-content:space-between;align-items:flex-end;border-top:1px solid var(--line);padding-top:10px}
.quote-name{font-size:10px;font-weight:700}
.quote-role{font-size:9px;color:var(--muted)}
.stars{color:var(--star);font-size:11px;letter-spacing:1px}
.slider-arrow{position:absolute;top:100px;width:22px;height:40px}
.dots{position:absolute;top:432px;left:582px;display:flex;gap:8px}
.dots span{width:9px;height:9px;border-radius:50%;background:#c9cde3}
.dots span.on{background:var(--blue)}

/* partners */
.partners{top:2680px}
.partner-row{display:flex;justify-content:center;align-items:center;gap:70px;margin-top:70px}
.partner-name{font-size:22px;font-weight:700;color:var(--navy)}

/* footer */
.site-footer{top:3040px;height:352px}
.footer-brand{position:absolute;left:232px;top:40px}
.footer-about{position:absolute;left:232px;top:96px;width:270px;font-size:10px;line-height:1.6;color:var(--text)}
.footer-about p+p{margin-top:10px}
.socials{position:absolute;left:232px;top:230px;display:flex;gap:10px}
.socials span{width:20px;height:20px;border-radius:50%;background:var(--blue)}
.footer-col{position:absolute;top:40px}
.footer-col h5{font-size:11px;font-weight:700;text-transform:uppercase}
.footer-col h5::after{content:"";display:block;width:30px;height:2px;background:var(--blue);margin-top:6px}
.footer-col ul{list-style:none;margin-top:18px}
.footer-col li{font-size:10px;color:var(--text);margin-bottom:13px}
.footer-col li::before{content:"›";color:var(--blue);margin-right:8px}
.contact-line{display:flex;gap:10px;align-items:flex-start;font-size:10px;color:var(--text);margin-top:18px;line-height:1.5}
.contact-line svg{flex:none}
.copyright{position:absolute;left:0;bottom:0;width:1200px;height:32px;border-top:1px solid var(--line);font-size:10px;color:var(--muted);text-align:center;line-height:32px}
</style>
</head>
<body>

<svg class="bg-waves" viewBox="0 0 1200 3392" aria-hidden="true">
  <rect width="1200" height="640" fill="#f3f4fc"/>
  <path d="M0 560 C260 470 520 720 800 610 C980 540 1100 600 1200 580 L1200 760 L0 760Z" fill="#fff"/>
  <path d="M0 1160 C120 1100 240 1180 220 1300 C200 1420 80 1480 0 1470Z" fill="var(--lavender)"/>
  <path d="M1200 1400 C1080 1480 1020 1660 1100 1800 C1140 1880 1200 1900 1200 1900Z" fill="var(--lavender)"/>
  <path d="M0 2980 C300 2900 600 3060 900 2990 C1050 2955 1140 2960 1200 2970 L1200 3392 L0 3392Z" fill="var(--lavender)"/>
</svg>

<header class="site-header">
  <div class="brand"><span class="brand-mark"></span>BrightHarbor</div>
  <nav class="main-nav">
    <span>HOME</span><span>MISSION</span><span>MEDIA</span><span>TEAM</span><span>LOCATIONS</span><span>SHOP</span><span>CONTACT</span>
    <span class="btn-login">LOGIN</span>
  </nav>
</header>

<section class="hero">
  <h1 class="hero-title">WE LET YOUR EMPLOYEES<br>FROM HOME</h1>
  <p class="hero-text">We develop an innovative VPN appliance (Model Vela Two) that gives every small business the possibility to let their employees work from home, safely and in minutes.</p>
  <span class="btn-primary">LEARN MORE</span>
  <div class="hero-art" role="img" aria-label="Illustration of connected network nodes in blue tones"></div>
</section>

<section class="features center">
  <div class="eyebrow">What our products</div>
  <h2 class="feature-title">"<strong>Vela Two</strong>" products are rolled out in minutes.</h2>
  <div class="feature-row">
    <article class="feature-card">
      <div class="feature-art" role="img" aria-label="Illustration of an employee connected to colleagues"></div>
      <h3>Employees can connect directly</h3>
      <p>Secure access to company tools straight from any home laptop.</p>
    </article>
    <article class="feature-card">
      <div class="feature-art" role="img" aria-label="Illustration of a person working at a desk"></div>
      <h3>Work from any location</h3>
      <p>One stable connection wherever your team chooses to work.</p>
    </article>
    <article class="feature-card">
      <div class="feature-art" role="img" aria-label="Illustration of a person beside a locked screen"></div>
      <h3>No change the company firewall</h3>
      <p>Plug it in and keep your existing network rules untouched.</p>
    </article>
  </div>
</section>

<section class="how">
  <div class="how-head">
    <div class="eyebrow">The use</div>
    <h2 class="section-title left">How It Works</h2>
  </div>
  <div class="connector" style="left:354px;top:376px;width:54px"></div>
  <div class="connector" style="left:618px;top:376px;width:54px"></div>
  <div class="connector" style="left:248px;top:496px;width:2px;height:48px"></div>
  <div class="connector" style="left:354px;top:664px;width:22px"></div>

  <div class="step" style="left:144px;top:256px">
    <span class="step-num">1</span>
    <svg class="step-icon" viewBox="0 0 54 54"><rect x="6" y="10" width="42" height="28" rx="3" fill="none" stroke="var(--blue)" stroke-width="2.5"/><path d="M20 46h14M27 38v8" stroke="var(--blue)" stroke-width="2.5"/><circle cx="27" cy="24" r="6" fill="var(--cyan)"/></svg>
    <h4>Go to our page</h4>
    <p>Visit the shop and read how the appliance fits your team.</p>
  </div>
  <div class="step" style="left:408px;top:256px">
    <span class="step-num">2</span>
    <svg class="step-icon" viewBox="0 0 54 54"><path d="M8 18 27 8l19 10v20L27 48 8 38Z" fill="none" stroke="var(--blue)" stroke-width="2.5"/><path d="M8 18l19 10 19-10M27 28v20" stroke="var(--blue)" stroke-width="2.5" fill="none"/></svg>
    <h4>Select product</h4>
    <p>Choose the model that matches the size of your business.</p>
  </div>
  <div class="step" style="left:672px;top:256px">
    <span class="step-num">3</span>
    <svg class="step-icon" viewBox="0 0 54 54"><rect x="10" y="6" width="34" height="42" rx="3" fill="none" stroke="var(--blue)" stroke-width="2.5"/><path d="M18 18h18M18 26h18M18 34h10" stroke="var(--cyan)" stroke-width="2.5"/></svg>
    <h4>Select product</h4>
    <p>Place your order and receive the appliance within days.</p>
  </div>
  <div class="step" style="left:144px;top:544px">
    <span class="step-num">4</span>
    <svg class="step-icon" viewBox="0 0 54 54"><rect x="6" y="18" width="42" height="18" rx="3" fill="none" stroke="var(--blue)" stroke-width="2.5"/><circle cx="15" cy="27" r="2.5" fill="var(--cyan)"/><circle cx="24" cy="27" r="2.5" fill="var(--cyan)"/><circle cx="33" cy="27" r="2.5" fill="var(--cyan)"/><path d="M27 36v10" stroke="var(--blue)" stroke-width="2.5"/></svg>
    <h4>Connect to any switch</h4>
    <p>Plug it into any switch inside your company network.</p>
  </div>
  <div class="step" style="left:376px;top:544px">
    <span class="step-num">5</span>
    <svg class="step-icon" viewBox="0 0 54 54"><rect x="8" y="10" width="38" height="26" rx="3" fill="none" stroke="var(--blue)" stroke-width="2.5"/><path d="M4 42h46" stroke="var(--blue)" stroke-width="2.5"/><path d="M27 16v12M21 23l6 6 6-6" stroke="var(--cyan)" stroke-width="2.5" fill="none"/></svg>
    <h4>Install software</h4>
    <p>Set up the client on each laptop for instant connection.</p>
  </div>
</section>

<section class="testimonials center">
  <div class="eyebrow">What customers are saying</div>
  <h2 class="section-title centered">Testimonials</h2>
  <div class="quotes">
    <svg class="slider-arrow" style="left:34px" viewBox="0 0 22 40"><path d="M18 4 4 20l14 16" stroke="var(--blue)" stroke-width="4" fill="none"/></svg>
    <article class="quote-card" style="left:76px;text-align:left">
      <div class="avatar" role="img" aria-label="Customer portrait"></div>
      <p class="quote-lead">" I am first these guys again "</p>
      <p class="quote-body">Setup took ten minutes and our whole office was working from home the same afternoon. Support answered every question quickly.</p>
      <div class="quote-meta"><div><div class="quote-name">CLARA DENHOLM</div><div class="quote-role">Founder of the company</div></div><span class="stars">★★★★★</span></div>
    </article>
    <article class="quote-card" style="left:408px;text-align:left">
      <div class="avatar" role="img" aria-label="Customer portrait"></div>
      <p class="quote-lead">" I am first these guys again "</p>
      <p class="quote-body">We never touched our firewall. The appliance just works and our staff connect securely from anywhere they need to be.</p>
      <div class="quote-meta"><div><div class="quote-name">MARTIN KESSLER</div><div class="quote-role">Owner of the company</div></div><span class="stars">★★★★★</span></div>
    </article>
    <article class="quote-card" style="left:752px;width:376px;text-align:left">
      <div class="avatar" role="img" aria-label="Customer portrait"></div>
      <p class="quote-lead">" I am first these guys again "</p>
      <p class="quote-body">A simple and reliable way to keep a small team productive at home. We ordered a second unit for our other branch.</p>
      <div class="quote-meta"><div><div class="quote-name">LENA HOFFAND</div><div class="quote-role">Manager of the company</div></div><span class="stars">★★★★★</span></div>
    </article>
    <svg class="slider-arrow" style="left:1144px" viewBox="0 0 22 40"><path d="M4 4l14 16L4 36" stroke="var(--blue)" stroke-width="4" fill="none"/></svg>
  </div>
  <div class="dots"><span class="on"></span><span></span></div>
</section>

<section class="partners center">
  <div class="eyebrow">We have a wonderful history</div>
  <h2 class="section-title centered">Our partners</h2>
  <div class="partner-row">
    <span class="partner-name">Norvale</span>
    <span class="partner-name">Copperleaf</span>
    <span class="partner-name">Sunmill</span>
    <span class="partner-name">Edgeworth</span>
    <span class="partner-name">Maison Ardel</span>
  </div>
</section>

<footer class="site-footer">
  <div class="footer-brand brand"><span class="brand-mark"></span>BrightHarbor</div>
  <div class="footer-about">
    <p>We build secure appliances that connect small businesses with their remote employees, quickly and without changes to existing networks.</p>
    <p>Reliable hardware, simple software and friendly support for every team working from home.</p>
  </div>
  <div class="socials"><span></span><span></span><span></span></div>

  <div class="footer-col" style="left:600px">
    <h5>Quick links</h5>
    <ul><li>Home</li><li>Blog</li><li>About Us</li><li>Contact Us</li><li>Terms</li><li>Privacy Policy</li><li>Sitemap</li></ul>
  </div>
  <div class="footer-col" style="left:812px">
    <h5>Let's connect</h5>
    <div class="contact-line"><svg width="14" height="14" viewBox="0 0 14 14"><path d="M3 1h3l1 3-2 1a7 7 0 0 0 4 4l1-2 3 1v3a1 1 0 0 1-1 1A12 12 0 0 1 2 2a1 1 0 0 1 1-1Z" fill="var(--blue)"/></svg><span>+1 555 014 2290</span></div>
    <div class="contact-line"><svg width="14" height="14" viewBox="0 0 14 14"><path d="M7 1a4.5 4.5 0 0 1 4.5 4.5C11.5 9 7 13 7 13S2.5 9 2.5 5.5A4.5 4.5 0 0 1 7 1Z" fill="var(--blue)"/><circle cx="7" cy="5.5" r="1.6" fill="#fff"/></svg><span>Harbor Street 12<br>Lakeside 4021</span></div>
    <div class="contact-line"><svg width="14" height="14" viewBox="0 0 14 14"><rect x="1" y="3" width="12" height="8" rx="1" fill="var(--blue)"/><path d="M1.5 3.5 7 8l5.5-4.5" stroke="#fff" fill="none"/></svg><span>hello@brightharbor.example</span></div>
  </div>
  <div class="copyright">© 2024 BrightHarbor</div>
</footer>

</body>
</html>
```